KORVENTLY.COM - BOTMOTIVE SALES

After the succesfully created logo for our new startup, we want to have a wordpress design according to the logo and the colours.

The company focussing on sales with AI based conversations. Focussing on social media. Furthermore it will offer whitelabeled BOT - MOTIVE sales activities based on ChatGPT and Bard.

Target Market(s)

Tech companies / Mid market IT staff

Coding

Coded - Design and coding required

Requirements
Must have
• AI pictures

```html
<!DOCTYPE html>
<html lang="en">
<head>
<meta charset="utf-8">
<title>Korvently — Botmotive Sales</title>
<link href="https://fonts.googleapis.com/css2?family=Rubik:wght@500;600;700&family=Inter:wght@400;500;600;700&display=swap" rel="stylesheet">
<style>
:root{
  --navy:#1f2a4c;
  --deep:#0e335f;
  --footer:#1b2d55;
  --teal:#4596a6;
  --ice:#eaf3fb;
  --ink:#1d2230;
  --body:#4a4f5c;
  --white:#ffffff;
  --line:#c9d6e2;
  --pro-line:#7fb7c2;
}
*{margin:0;padding:0;box-sizing:border-box}
html,body{width:1200px;height:5147px;overflow:hidden}
body{position:relative;font-family:"Inter",sans-serif;color:var(--ink);background:var(--white)}
.abs{position:absolute}
h1,h2,h3{font-family:"Rubik",sans-serif;font-weight:600}
p{font-size:11.5px;line-height:21px;color:var(--body)}

.topnav{left:0;top:0;width:1200px;height:50px;background:var(--navy);display:flex;justify-content:center;align-items:center;gap:44px}
.topnav a{color:#e4e8f2;font-size:11px;text-decoration:none}
.topnav .dot{width:6px;height:6px;border-radius:50%;background:var(--teal)}

.hero{left:0;top:50px;width:1200px;height:634px;overflow:hidden}
.hero-photo{position:absolute;inset:0;background:linear-gradient(120deg,#c9c2b6 30%,#8a8f96 55%,#2f4f8f 72%,#d8d2c8 90%)}
.hero-shape{position:absolute;inset:0}
.brand{color:var(--white);font-family:"Rubik",sans-serif;font-weight:600;font-size:20px;letter-spacing:1px;display:flex;align-items:center;gap:8px}
.brand .mark{width:14px;height:14px;border-radius:50%;background:var(--white)}
.hero h1{left:124px;top:196px;width:460px;font-size:44px;line-height:47px;color:var(--white)}
.hero p{left:124px;top:366px;width:380px;color:#eef6f8;font-size:10.5px;line-height:19px}
.btn{display:flex;align-items:center;justify-content:center;font-weight:600;font-size:11px;text-decoration:none}
.btn-navy{background:var(--navy);color:var(--white)}

.split h2{font-size:36px;line-height:46px;color:var(--ink)}
.split p{width:400px;margin-top:18px}

.ai-band{left:0;top:1392px;width:1200px;height:612px;background:radial-gradient(circle at 30% 50%,#2f6fb8 0,#143a6e 30%,#0a1a33 60%,#150c0c 100%)}
.ai-band h2{color:var(--white)}
.ai-band p{color:#e6ecf4}

.section-title{width:1200px;text-align:center;font-size:36px;color:var(--ink)}
.section-sub{width:680px;left:260px;text-align:center;font-size:10.5px;line-height:19px}

.plan-ribbon{height:56px;background:var(--deep);color:var(--white);font-family:"Rubik",sans-serif;font-weight:500;font-size:25px;display:flex;align-items:center;justify-content:center}
.price{font-family:"Rubik",sans-serif;font-weight:500;font-size:42px;text-align:center}
.plan-desc{text-align:center;font-size:15px;line-height:28px}
.features{list-style:none}
.features li{height:48px;display:flex;justify-content:space-between;align-items:center;font-size:15px;font-weight:600;border-bottom:1px solid var(--line)}
.features li:last-child{border-bottom:none}
.features.pro li{border-color:var(--pro-line)}
.tick{width:18px;height:18px}

.statement{left:0;top:3370px;width:1200px;height:798px;background:var(--deep);overflow:hidden}
.statement .section-title{color:var(--white)}
.statement .section-sub{color:#dfe7f2}
.card{width:304px;height:440px;background:var(--white);border-radius:6px}
.card .photo{position:absolute;left:14px;top:14px;width:276px;height:182px;background:linear-gradient(180deg,#e8e8e6,#cfd3d6)}
.card .play{position:absolute;left:212px;top:166px;width:56px;height:56px;border-radius:50%;background:var(--deep);border:4px solid var(--white)}
.card h3{position:absolute;left:30px;top:236px;font-size:17px;line-height:21px;color:var(--deep)}
.card p{position:absolute;left:30px;top:292px;width:240px;font-size:12px;line-height:22px}
.card .more{position:absolute;left:30px;top:396px;font-size:10.5px;font-weight:600;color:var(--teal)}

.footer{left:0;top:4870px;width:1200px;height:277px;background:var(--footer)}
.footer nav{position:absolute;left:494px;top:108px;display:flex;gap:36px}
.footer nav a{color:#e4e8f2;font-size:12px;text-decoration:none}
.footer .copy{position:absolute;left:906px;top:164px;color:#e4e8f2;font-size:12px}
</style>
</head>
<body>

<nav class="abs topnav">
  <a href="#sales">Sales Personal</a><span class="dot"></span>
  <a href="#social">BOTMOTIVE Social Media</a><span class="dot"></span>
  <a href="#pricing">Pricing</a><span class="dot"></span>
  <a href="#statement">Statement</a><span class="dot"></span>
  <a href="#philosophy">Philosophy</a>
</nav>

<header class="abs hero">
  <div class="hero-photo" role="img" aria-label="Photo of a young businessman in a blue blazer writing in a notebook while checking his phone"></div>
  <svg class="hero-shape" width="1200" height="634" viewBox="0 0 1200 634"><polygon points="0,0 600,0 720,160 820,634 0,634" fill="#4596a6"/></svg>
  <div class="abs brand" style="left:124px;top:78px"><span class="mark"></span>KORVENTLY</div>
  <h1 class="abs">Where AI Meets Conversations For Success</h1>
  <p class="abs">Lorem Ipsum is simply dummy text of the printing and typesetting industry. Lorem Ipsum has been the industry's standard dummy text ever since the 1500s, when an unknown printer took a galley of type and scrambled it to make a type specimen book.</p>
  <a class="abs btn btn-navy" href="#pricing" style="left:124px;top:476px;width:214px;height:44px">Automate All Prospecting</a>
</header>

<section id="sales" class="split">
  <div class="abs" style="left:124px;top:784px;width:466px;height:508px;background:linear-gradient(135deg,#1b2b34,#2d3d44 50%,#6a4f3a)" role="img" aria-label="AI picture of a woman's profile overlaid with a glowing digital face-scan interface"></div>
  <div class="abs" style="left:648px;top:842px">
    <h2>Sales Personal</h2>
    <p>Lorem Ipsum is simply dummy text of the printing and typesetting industry. Lorem Ipsum has been the industry's standard dummy text ever since the 1500s, when an unknown printer took a galley of type and scrambled it to make a type specimen book. It has survived not only five centuries, but also the leap into electronic typesetting, remaining essentially unchanged.</p>
    <p>It was popularised in the 1960s with the release of Typeleaf sheets containing Lorem Ipsum passages, and more recently with desktop publishing software like Folio PageSet including versions of Lorem Ipsum.</p>
  </div>
  <a class="abs btn btn-navy" href="#pricing" style="left:648px;top:1178px;width:212px;height:44px">Click For Learn More</a>
</section>

<section id="social" class="abs ai-band split" role="img" aria-label="AI picture of a hand holding a glowing smartphone showing an artificial intelligence assistant">
  <div class="abs" style="left:648px;top:118px">
    <h2>BOTMOTIVE Social<br>Media</h2>
    <p>Lorem Ipsum is simply dummy text of the printing and typesetting industry. Lorem Ipsum has been the industry's standard dummy text ever since the 1500s, when an unknown printer took a galley of type and scrambled it to make a type specimen book. It has survived not only five centuries, but also the leap into electronic typesetting, remaining essentially unchanged.</p>
    <p>It was popularised in the 1960s with the release of Typeleaf sheets containing Lorem Ipsum passages, and more recently with desktop publishing software like Folio PageSet including versions of Lorem Ipsum.</p>
  </div>
</section>

<section id="pricing">
  <h2 class="abs section-title" style="left:0;top:2092px">Pricing</h2>
  <p class="abs section-sub" style="top:2162px">It was popularised in the 1960s with the release of Typeleaf sheets containing Lorem Ipsum passages, and more recently with desktop publishing software like Folio PageSet including versions of Lorem Ipsum.</p>

  <div class="abs" style="left:120px;top:2332px;width:446px;height:904px;background:var(--ice)"></div>
  <svg class="abs" style="left:106px;top:2420px" width="14" height="14"><polygon points="0,0 14,0 14,14" fill="#0a2448"/></svg>
  <div class="abs plan-ribbon" style="left:106px;top:2364px;width:432px">STARTER</div>
  <div class="abs price" style="left:120px;top:2454px;width:446px;color:var(--deep)">$ 14.39</div>
  <p class="abs plan-desc" style="left:193px;top:2540px;width:300px">Lorem Ipsum is simply dummy text of the printing and typesetting industry. Lorem Ipsum has been the industry's standard dummy text ever since the 1500s,</p>
  <ul class="abs features" style="left:192px;top:2702px;width:300px;color:var(--ink)">
    <li>Lorem Ipsum<svg class="tick" viewBox="0 0 18 18"><circle cx="9" cy="9" r="7" fill="none" stroke="#4596a6" stroke-width="1.3"/><path d="M5.8 9.2l2.2 2.2 4.2-4.4" fill="none" stroke="#4596a6" stroke-width="1.4"/></svg></li>
    <li>Lorem Ipsum<svg class="tick" viewBox="0 0 18 18"><circle cx="9" cy="9" r="7" fill="none" stroke="#4596a6" stroke-width="1.3"/><path d="M5.8 9.2l2.2 2.2 4.2-4.4" fill="none" stroke="#4596a6" stroke-width="1.4"/></svg></li>
    <li>Lorem Ipsum<svg class="tick" viewBox="0 0 18 18"><circle cx="9" cy="9" r="7" fill="none" stroke="#4596a6" stroke-width="1.3"/><path d="M5.8 9.2l2.2 2.2 4.2-4.4" fill="none" stroke="#4596a6" stroke-width="1.4"/></svg></li>
    <li>Lorem Ipsum<svg class="tick" viewBox="0 0 18 18"><circle cx="9" cy="9" r="7" fill="none" stroke="#4596a6" stroke-width="1.3"/><path d="M5.8 9.2l2.2 2.2 4.2-4.4" fill="none" stroke="#4596a6" stroke-width="1.4"/></svg></li>
    <li>Lorem Ipsum<svg class="tick" viewBox="0 0 18 18"><circle cx="9" cy="9" r="7" fill="none" stroke="#4596a6" stroke-width="1.3"/><path d="M5.8 9.2l2.2 2.2 4.2-4.4" fill="none" stroke="#4596a6" stroke-width="1.4"/></svg></li>
    <li>Lorem Ipsum<svg class="tick" viewBox="0 0 18 18"><circle cx="9" cy="9" r="7" fill="none" stroke="#4596a6" stroke-width="1.3"/><path d="M5.8 9.2l2.2 2.2 4.2-4.4" fill="none" stroke="#4596a6" stroke-width="1.4"/></svg></li>
    <li>Lorem Ipsum<svg class="tick" viewBox="0 0 18 18"><circle cx="9" cy="9" r="7" fill="none" stroke="#4596a6" stroke-width="1.3"/><path d="M5.8 9.2l2.2 2.2 4.2-4.4" fill="none" stroke="#4596a6" stroke-width="1.4"/></svg></li>
  </ul>
  <a class="abs btn" href="#" style="left:166px;top:3142px;width:352px;height:56px;background:var(--teal);color:var(--white);font-size:16px;letter-spacing:1px">START FREE TRIAL</a>

  <div class="abs" style="left:590px;top:2290px;width:460px;height:980px;background:var(--teal)"></div>
  <svg class="abs" style="left:576px;top:2376px" width="14" height="14"><polygon points="0,0 14,0 14,14" fill="#0a2448"/></svg>
  <div class="abs plan-ribbon" style="left:576px;top:2320px;width:430px">PRO</div>
  <div class="abs" style="left:1020px;top:2262px;width:60px;height:60px;border-radius:50%;background:#c8323a;border:4px solid var(--white)"></div>
  <div class="abs price" style="left:590px;top:2408px;width:460px;color:var(--white)">$ 44.99</div>
  <p class="abs plan-desc" style="left:661px;top:2494px;width:318px;color:#f0f7f9">Lorem Ipsum is simply dummy text of the printing and typesetting industry. Lorem Ipsum has been the industry's standard dummy text ever since the 1500s,</p>
  <ul class="abs features pro" style="left:670px;top:2690px;width:300px;color:var(--white)">
    <li>Lorem Ipsum<svg class="tick" viewBox="0 0 18 18"><circle cx="9" cy="9" r="7" fill="none" stroke="#fff" stroke-width="1.3"/><path d="M5.8 9.2l2.2 2.2 4.2-4.4" fill="none" stroke="#fff" stroke-width="1.4"/></svg></li>
    <li>Lorem Ipsum<svg class="tick" viewBox="0 0 18 18"><circle cx="9" cy="9" r="7" fill="none" stroke="#fff" stroke-width="1.3"/><path d="M5.8 9.2l2.2 2.2 4.2-4.4" fill="none" stroke="#fff" stroke-width="1.4"/></svg></li>
    <li>Lorem Ipsum<svg class="tick" viewBox="0 0 18 18"><circle cx="9" cy="9" r="7" fill="none" stroke="#fff" stroke-width="1.3"/><path d="M5.8 9.2l2.2 2.2 4.2-4.4" fill="none" stroke="#fff" stroke-width="1.4"/></svg></li>
    <li>Lorem Ipsum<svg class="tick" viewBox="0 0 18 18"><circle cx="9" cy="9" r="7" fill="none" stroke="#fff" stroke-width="1.3"/><path d="M5.8 9.2l2.2 2.2 4.2-4.4" fill="none" stroke="#fff" stroke-width="1.4"/></svg></li>
    <li>Lorem Ipsum<svg class="tick" viewBox="0 0 18 18"><circle cx="9" cy="9" r="7" fill="none" stroke="#fff" stroke-width="1.3"/><path d="M5.8 9.2l2.2 2.2 4.2-4.4" fill="none" stroke="#fff" stroke-width="1.4"/></svg></li>
    <li>Lorem Ipsum<svg class="tick" viewBox="0 0 18 18"><circle cx="9" cy="9" r="7" fill="none" stroke="#fff" stroke-width="1.3"/><path d="M5.8 9.2l2.2 2.2 4.2-4.4" fill="none" stroke="#fff" stroke-width="1.4"/></svg></li>
    <li>Lorem Ipsum<svg class="tick" viewBox="0 0 18 18"><circle cx="9" cy="9" r="7" fill="none" stroke="#fff" stroke-width="1.3"/><path d="M5.8 9.2l2.2 2.2 4.2-4.4" fill="none" stroke="#fff" stroke-width="1.4"/></svg></li>
    <li>Lorem Ipsum<svg class="tick" viewBox="0 0 18 18"><circle cx="9" cy="9" r="7" fill="none" stroke="#fff" stroke-width="1.3"/><path d="M5.8 9.2l2.2 2.2 4.2-4.4" fill="none" stroke="#fff" stroke-width="1.4"/></svg></li>
  </ul>
  <a class="abs btn" href="#" style="left:644px;top:3174px;width:352px;height:56px;background:var(--white);color:var(--deep);font-size:16px;letter-spacing:1px">JOIN</a>
</section>

<section id="statement" class="abs statement">
  <h2 class="abs section-title" style="left:0;top:96px">Statement</h2>
  <p class="abs section-sub" style="top:160px">It was popularised in the 1960s with the release of Typeleaf sheets containing Lorem Ipsum passages, and more recently with desktop publishing software like Folio PageSet including versions of Lorem Ipsum.</p>

  <article class="abs card" style="left:124px;top:256px">
    <div class="photo" role="img" aria-label="Portrait photo of a smiling man with crossed arms"></div>
    <svg class="play" viewBox="0 0 48 48"><polygon points="19,15 34,24 19,33" fill="#fff"/></svg>
    <h3>Smith<br>Johnson</h3>
    <p>Lorem Ipsum is simply dummy text of the printing and typesetting industry. Lorem Ipsum has been the industry's standard.</p>
    <span class="more">LOREM IPSUM</span>
  </article>
  <article class="abs card" style="left:448px;top:256px">
    <div class="photo" style="background:linear-gradient(180deg,#a9c88a,#6f8f5a)" role="img" aria-label="Portrait photo of a smiling blonde businesswoman outdoors"></div>
    <svg class="play" viewBox="0 0 48 48"><polygon points="19,15 34,24 19,33" fill="#fff"/></svg>
    <h3>Smith<br>Johnson</h3>
    <p>Lorem Ipsum is simply dummy text of the printing and typesetting industry. Lorem Ipsum has been the industry's standard.</p>
    <span class="more">LOREM IPSUM</span>
  </article>
  <article class="abs card" style="left:772px;top:256px">
    <div class="photo" style="background:linear-gradient(180deg,#ececec,#e3d2d2)" role="img" aria-label="Portrait photo of a smiling woman in a red top"></div>
    <svg class="play" viewBox="0 0 48 48"><polygon points="19,15 34,24 19,33" fill="#fff"/></svg>
    <h3>Smith<br>Johnson</h3>
    <p>Lorem Ipsum is simply dummy text of the printing and typesetting industry. Lorem Ipsum has been the industry's standard.</p>
    <span class="more">LOREM IPSUM</span>
  </article>
</section>

<section id="philosophy" class="split">
  <div class="abs" style="left:124px;top:4266px;width:466px;height:508px;background:radial-gradient(circle at 45% 45%,#4aa3c8 0,#1e4a6e 30%,#0e1d33 70%)" role="img" aria-label="AI picture of a finger touching a glowing digital brain interface"></div>
  <div class="abs" style="left:648px;top:4324px">
    <h2>Philosophy</h2>
    <p>Lorem Ipsum is simply dummy text of the printing and typesetting industry. Lorem Ipsum has been the industry's standard dummy text ever since the 1500s, when an unknown printer took a galley of type and scrambled it to make a type specimen book. It has survived not only five centuries, but also the leap into electronic typesetting, remaining essentially unchanged.</p>
    <p>It was popularised in the 1960s with the release of Typeleaf sheets containing Lorem Ipsum passages, and more recently with desktop publishing software like Folio PageSet including versions of Lorem Ipsum.</p>
  </div>
  <a class="abs btn btn-navy" href="#pricing" style="left:648px;top:4660px;width:212px;height:44px">Click For Learn More</a>
</section>

<footer class="abs footer">
  <div class="abs brand" style="left:120px;top:112px;font-size:26px"><span class="mark"></span>KORVENTLY</div>
  <nav>
    <a href="#sales">Sales Personal</a>
    <a href="#social">BOTMOTIVE Social Media</a>
    <a href="#pricing">Pricing</a>
    <a href="#statement">Statement</a>
    <a href="#philosophy">Philosophy</a>
  </nav>
  <div class="copy">Copyright@2023-Korvently</div>
</footer>

</body>
</html>
```